MODERN + COOL Business Card Needed!

SUMMARY
This is for a 40+ year old family business that is transitioning to the 2nd generation and is in real need of a more modern facelift. Ive attached a company logo (I made quickly as an idea with my limited PSD skills) to start off with that you are welcome to change and draw ideas from. Ive also attached some screen shots of cards I like to give you an idea of my preferences.

WHAT WE DO
The company name is Tall Pine HK Ltd. But I prefer to just call it Tall Pine or Tall Pine with Harbour Vale as kind of a sub heading on the business card. We own a factory as well as help our customers find factories to make their product. Product I mean, toys 99.9% of the time. Simple old school toys like board games, puzzles, wooden toys, baby/infant toys.

You can say we are a "sourcing" or "trading" or "consulting" company with a factory to help you do it. But since we deal with toys, i like to keep it modern and cool and fun, not serious like managing hedge funds.

WHAT WE ARE LOOKING FOR
A cool, unique looking business card that stands out. In terms of design, something modern and professional. I like darker colored cards and I like colors such as blue/green/dark gray, but am open to other colored themes. I Like bright lime green with gray, always though thats a nice combo. I prefer cards that are all colored and not so much white showing (I think). Ive attached a few screenshots of cards so take a look to get a feel of what I like.

We do alot of wooden stacking games in variety of colors too like Tovra, Lumo, Towerplix (google these to check them out). So designs that sort of resemble stacking or building would be cool but totally not necessary.

In terms of the physical aspects of the card, Im looking for a card a bit different than the standard rectangular shape. Double sided. Little things like having corner(s) be round or different angle instead of square edge I always thought was nice. Its got to be mostly a normal card size, no folding or smaller cards that fit weird in your wallet. No vertical designs. Am open to VERY different/creative shapes (as long as it still fits in a wallet good like a normal buisness card.
Updates

Hi everyone!

Just wanted to write a message to everyone to let them know all submissions are being reviewed or have been reviewed.  If I have not responded with feedback, rest assure your submission was definitely looked at in detail but I either have just been too busy to respond (alot of submissions!), or its on my to be considered list.

I respect and really enjoy receiving everyones creativity and work so I dont want it to go unrecognized - thus this message!  Feel free to submit more ideas if you like until this project ends.  Sometimes some designs just dont click but sometimes they can so you never know!

Thanks again for everyones participation and great work!

~Dev Orr

Target Market(s)

The cards are mainly handed to toy company sourcers and buyers. People I talk to ... say Pelvane for example... might want to make their next edition of Farthingale game with a reputable factory at a good cost so they can sell it to stores at a profit.

So these are the types of people I often try to talk and introduce myself and my company to.

Industry/Entity Type

Building

Colors
acd036
0392cd
00a88e
474747
606060

Requirements
Must have
• Just double sided, not plain rectangle corners, and just cool to look at and catches your eye!

Oh and the obvious business card stuff like place for name, address, number, email, etc.
Nice to have
• Think more modern and fun, not serious and old fashion (thats what we used to be!). Can use the logo I attached and you can definitely alter and change the logo or make a whole new one!

Oh and can definitely use a creative slogan if you like to think of one based on what I described in what we do.
Should not have
• Dont use fonts or text placement that might make "Tall Pine" look like "Tal Lpine"... We arent selling news papers!!

Please nothing related to education since we have the word Pine in the title, thats not our business at all.

Logo and design should not be too heavy on things related to toys, as though thats what we primarily focus on now, what we do may change over time.

```html
<!DOCTYPE html>
<html lang="en">
<head>
<meta charset="utf-8">
<title>Tall Pine Ltd. — Business Card</title>
<link rel="stylesheet" href="https://fonts.googleapis.com/css2?family=Open+Sans:ital,wght@0,400;0,600;1,400&family=Russo+One&display=swap">
<style>
  :root {
    --backdrop: #2e2e2e;
    --teal-light: #47999b;
    --teal: #237d80;
    --teal-deep: #0f5359;
    --mist: #c9d7db;
    --paper: #ededed;
    --paper-shade: #dcdcdc;
    --slate: #7f9196;
    --rule: #b7c9cc;
    --ink: #2f2f2f;
    --ink-soft: #555555;
    --white: #ffffff;
  }
  html, body {
    margin: 0;
    width: 1200px;
    height: 900px;
    overflow: hidden;
    background: var(--backdrop);
  }
  .canvas {
    position: relative;
    width: 1200px;
    height: 900px;
  }
  .card {
    position: absolute;
    width: 560px;
    height: 320px;
    border-radius: 6px;
    overflow: hidden;
    box-shadow: 0 12px 30px rgba(0,0,0,.45);
  }
  .card--back { left: 110px; top: 110px; }
  .card--front { left: 530px; top: 470px; }
  .card svg { position: absolute; inset: 0; display: block; }

  .wordmark {
    position: absolute;
    color: var(--white);
    font-family: "Russo One", sans-serif;
    font-weight: 400;
    line-height: 1;
    white-space: nowrap;
  }
  .wordmark__name,
  .wordmark__place { display: block; }

  .card--front .wordmark { left: 230px; bottom: 30px; }
  .card--front .wordmark__name { font-size: 38px; }
  .card--front .wordmark__place { font-size: 22px; margin-top: 6px; }

  .card--back .wordmark { left: 150px; bottom: 30px; }
  .card--back .wordmark__name { font-size: 30px; }
  .card--back .wordmark__place { font-size: 18px; margin-top: 5px; }

  .contact {
    position: absolute;
    left: 40px;
    top: 28px;
    font-family: "Open Sans", sans-serif;
    color: var(--ink);
  }
  .contact__name { margin: 0; font-size: 21px; font-weight: 400; }
  .contact__role { margin: 0 0 12px; font-size: 13px; font-style: italic; color: var(--ink-soft); }
  .contact__list { margin: 0; padding: 0; list-style: none; font-size: 12.5px; line-height: 1.45; }
</style>
</head>
<body>
<main class="canvas">

  <section class="card card--back" aria-label="Card back with contact details">
    <svg viewBox="0 0 560 320" width="560" height="320" aria-hidden="true">
      <defs>
        <linearGradient id="paperGrad" x1="0" y1="0" x2="1" y2="1">
          <stop offset="0" stop-color="var(--paper-shade)"/>
          <stop offset="1" stop-color="var(--paper)"/>
        </linearGradient>
        <linearGradient id="backTeal" x1="0" y1="0" x2="1" y2="1">
          <stop offset="0" stop-color="var(--teal)"/>
          <stop offset="1" stop-color="var(--teal-deep)"/>
        </linearGradient>
      </defs>
      <rect width="560" height="320" fill="url(#backTeal)"/>
      <polygon points="0,0 560,0 560,55 0,215" fill="url(#paperGrad)"/>
      <polygon points="0,215 300,130 240,230 0,292" fill="var(--slate)"/>
      <line x1="240" y1="230" x2="560" y2="140" stroke="var(--rule)" stroke-width="1"/>
      <polygon points="330,198 560,140 560,148 334,206" fill="var(--slate)" opacity=".8"/>
    </svg>
    <div class="contact">
      <h2 class="contact__name">Your Name</h2>
      <p class="contact__role">Position</p>
      <ul class="contact__list">
        <li>Address: xxxxxxxxxxxxxxxx</li>
        <li>Phone: xxxxxxxxxxxxxxxxx</li>
        <li>Email: xxxxxxxxxxxxxxxx</li>
        <li>Web: xxxxxxxxxxxxxx</li>
      </ul>
    </div>
    <div class="wordmark">
      <span class="wordmark__name">tall pine ltd</span>
      <span class="wordmark__place">harbour vale</span>
    </div>
  </section>

  <section class="card card--front" aria-label="Card front with company name">
    <svg viewBox="0 0 560 320" width="560" height="320" aria-hidden="true">
      <defs>
        <linearGradient id="frontTeal" x1="0" y1="0" x2="1" y2="1">
          <stop offset="0" stop-color="var(--teal-light)"/>
          <stop offset=".55" stop-color="var(--teal)"/>
          <stop offset="1" stop-color="var(--teal-deep)"/>
        </linearGradient>
        <linearGradient id="mistGrad" x1="0" y1="0" x2="1" y2="1">
          <stop offset="0" stop-color="#dde6e8"/>
          <stop offset="1" stop-color="var(--mist)"/>
        </linearGradient>
      </defs>
      <rect width="560" height="320" fill="url(#frontTeal)"/>
      <polygon points="290,165 560,95 560,320 0,320 0,300" fill="#000" opacity=".08"/>
      <polygon points="0,130 290,165 0,300" fill="url(#mistGrad)"/>
      <line x1="0" y1="130" x2="290" y2="165" stroke="var(--rule)" stroke-width="1"/>
      <line x1="290" y1="165" x2="560" y2="95" stroke="var(--rule)" stroke-width="1"/>
      <line x1="290" y1="165" x2="560" y2="212" stroke="var(--rule)" stroke-width="1"/>
      <polygon points="345,168 560,198 560,206 343,176" fill="var(--slate)" opacity=".85"/>
    </svg>
    <div class="wordmark">
      <span class="wordmark__name">tall pine ltd</span>
      <span class="wordmark__place">harbour vale</span>
    </div>
  </section>

</main>
</body>
</html>
```